Banner Ad for Easter Sale

We want an Easter graphics and design that will look professional, attractive, suit our website.

We need the graphic to show our customers that we have a massive sale going on during the Easter long weekend. The sale will be for our pavers and retaining wall blocks range of products.

The dimensions are 691 x 281 pixels, and will need to have rounded edges, just like the ones that can be seen in the centre of our homepage: www.bramblecart.com.au.

This graphic will be the first to load up in the centre rotating images on the homepage.

When clicked on, the graphic will take the customer to a page that contains the discounted products. The products included in the sale are here:
http://www.bramblecart.com.au/Easter-Sale
Note that the prices may or may not change so the prices should be ignored.
Product images may be used but don't have to be used.

We would like for it to have the following texts:
"Massive Sale on this Easter Long Weekend"
"Click here to view products"
(in smaller writing) "Pavers and Retaining wall Sample Packs Reduced to $10" and in smaller writing have our long weekend contact hours:
"Extended Customer Service hours:
8am to 9pm Daily"
"Up to 50% off!"

We are open to the texts being varied.

Target Market(s)

DIY Enthusiasts, End Customers, Landscapers

Industry/Entity Type

Product

Requirements
Must have
• Dimensions being 691 x 281 pixels, and will need to have rounded edges, just like the ones that can be seen in the centre of our homepage: www.bramblecart.com.au.

```html
<!DOCTYPE html>
<html lang="en">
<head>
<meta charset="utf-8">
<title>Easter Long Weekend Sale – Bramblecart</title>
<link rel="stylesheet" href="https://fonts.googleapis.com/css2?family=Francois+One&family=Arimo:wght@400;700&family=Roboto:wght@400&display=swap">
<style>
  :root {
    --page: #ffffff;
    --stone-light: #e4d8c1;
    --stone-mid: #d9cbb0;
    --stone-dark: #cbb998;
    --stone-joint: #c2b08f;
    --ink: #0d0d0d;
    --pill-top: #ffffff;
    --pill-mid: #dedede;
    --pill-bottom: #a6a6a6;
    --pill-text: #1a1a1a;
    --burst-light: #d9ec52;
    --burst-dark: #8fc430;
    --burst-rim: #f3f7d8;
    --price-red: #c4161c;
    --offer-green: #5b7d2a;
    --button-red: #c0393f;
    --button-red-dark: #8e1f27;
    --button-text: #ffffff;
    --paper: #fbfaf6;
    --paper-shade: #c9c4b8;
    --egg-red: #c8302c;
    --egg-yellow: #e2b93a;
    --egg-blue: #6aa6d8;
    --egg-green: #8aa64a;
  }
  html, body {
    margin: 0;
    padding: 0;
    width: 1200px;
    height: 550px;
    overflow: hidden;
    background: var(--page);
  }
  .easter-banner { display: block; width: 1200px; height: 550px; }
  .headline { font-family: "Francois One", "Arial Narrow", sans-serif; fill: var(--ink); }
  .pill-label { font-family: "Roboto", Arial, sans-serif; fill: var(--pill-text); }
  .burst-label { font-family: "Arimo", Arial, sans-serif; font-weight: 700; fill: var(--ink); }
  .burst-price { font-family: "Francois One", Arial, sans-serif; fill: var(--price-red); }
  .hours-label { font-family: "Arimo", Arial, sans-serif; font-weight: 400; fill: var(--ink); }
  .hours-value { font-family: "Arimo", Arial, sans-serif; font-weight: 700; fill: var(--ink); }
  .offer-small { font-family: "Francois One", Arial, sans-serif; fill: var(--ink); }
  .offer-big { font-family: "Francois One", "Arial Narrow", sans-serif; fill: var(--offer-green); }
  .button-label { font-family: "Arimo", Arial, sans-serif; font-weight: 400; fill: var(--button-text); }
</style>
</head>
<body>
<a href="http://www.bramblecart.com.au/Easter-Sale" aria-label="Easter long weekend sale at www.bramblecart.com.au">
<svg class="easter-banner" viewBox="0 0 1200 550" xmlns="http://www.w3.org/2000/svg">
  <defs>
    <linearGradient id="stone-fill" x1="0" y1="0" x2="1" y2="1">
      <stop offset="0" stop-color="var(--stone-mid)"/>
      <stop offset="0.45" stop-color="var(--stone-light)"/>
      <stop offset="1" stop-color="var(--stone-dark)"/>
    </linearGradient>
    <linearGradient id="pill-fill" x1="0" y1="0" x2="0" y2="1">
      <stop offset="0" stop-color="var(--pill-top)"/>
      <stop offset="0.55" stop-color="var(--pill-mid)"/>
      <stop offset="1" stop-color="var(--pill-bottom)"/>
    </linearGradient>
    <radialGradient id="burst-fill" cx="0.45" cy="0.4" r="0.6">
      <stop offset="0" stop-color="var(--burst-light)"/>
      <stop offset="1" stop-color="var(--burst-dark)"/>
    </radialGradient>
    <linearGradient id="egg-photo-fill" x1="0" y1="0.2" x2="1" y2="0.8">
      <stop offset="0" stop-color="var(--egg-red)"/>
      <stop offset="0.35" stop-color="var(--egg-yellow)"/>
      <stop offset="0.7" stop-color="var(--egg-blue)"/>
      <stop offset="1" stop-color="var(--egg-green)"/>
    </linearGradient>
    <linearGradient id="curl-fill" x1="0" y1="0" x2="1" y2="0">
      <stop offset="0" stop-color="var(--paper-shade)"/>
      <stop offset="0.35" stop-color="var(--paper)"/>
      <stop offset="0.75" stop-color="#ffffff"/>
      <stop offset="1" stop-color="var(--paper-shade)"/>
    </linearGradient>
    <linearGradient id="button-fill" x1="0" y1="0" x2="0" y2="1">
      <stop offset="0" stop-color="var(--button-red)"/>
      <stop offset="1" stop-color="var(--button-red-dark)"/>
    </linearGradient>
    <clipPath id="banner-clip">
      <rect x="82" y="67" width="1050" height="426" rx="22"/>
    </clipPath>
  </defs>

  <g class="banner-frame" clip-path="url(#banner-clip)">
    <rect class="stone-backdrop" x="82" y="67" width="1050" height="426" fill="url(#stone-fill)"/>
    <g class="stone-joints" stroke="var(--stone-joint)" stroke-width="1.5" fill="none" opacity="0.55">
      <path d="M82 100 H1132"/>
      <path d="M440 180 H695 V493"/>
      <path d="M1020 210 V493"/>
    </g>

    <g class="torn-window">
      <path class="paper-edge" fill="var(--paper)"
        d="M82 126 L150 138 L230 160 L300 188 L360 202 L410 210 L420 226 L410 360 L395 372 L330 378 L250 394 L170 416 L120 432 L82 446 Z"/>
      <path class="egg-photo" role="img" aria-label="Photograph of brightly hand-painted Easter eggs"
        fill="url(#egg-photo-fill)"
        d="M82 134 L150 146 L228 168 L298 195 L358 209 L405 218 L402 360 L330 370 L248 386 L168 408 L118 424 L82 438 Z"/>
      <g class="paper-curl">
        <path fill="url(#curl-fill)" stroke="var(--paper-shade)" stroke-width="1"
          d="M398 220 C420 212 455 214 464 226 C468 240 464 280 458 320 C454 346 440 364 420 368 L396 368 C410 352 414 330 414 300 L412 236 C410 228 404 222 398 220 Z"/>
        <path fill="none" stroke="var(--paper-shade)" stroke-width="1.2"
          d="M404 350 C418 352 428 342 430 330"/>
        <path fill="none" stroke="var(--paper-shade)" stroke-width="1.2"
          d="M440 228 C452 240 452 300 446 330"/>
      </g>
    </g>
  </g>

  <g class="sample-pack-callout">
    <rect class="pill" x="330" y="115" width="600" height="46" rx="23" fill="url(#pill-fill)" stroke="#8c8c8c" stroke-width="1"/>
    <text class="pill-label" x="630" y="148" font-size="27" text-anchor="middle" textLength="536" lengthAdjust="spacingAndGlyphs">Pavers and Retaining wall Sample Packs</text>
  </g>

  <g class="price-burst" transform="translate(986 138)">
    <polygon fill="var(--burst-rim)"
      points="0,-70 12,-55 27,-64 32,-47 50,-50 47,-33 64,-27 54,-13 68,0 54,13 64,27 47,33 50,50 32,47 27,64 12,55 0,70 -12,55 -27,64 -32,47 -50,50 -47,33 -64,27 -54,13 -68,0 -54,-13 -64,-27 -47,-33 -50,-50 -32,-47 -27,-64 -12,-55"/>
    <polygon fill="url(#burst-fill)"
      points="0,-63 11,-49 24,-57 28,-42 44,-44 42,-29 57,-24 48,-12 60,0 48,12 57,24 42,29 44,44 28,42 24,57 11,49 0,63 -11,49 -24,57 -28,42 -44,44 -42,29 -57,24 -48,12 -60,0 -48,-12 -57,-24 -42,-29 -44,-44 -28,-42 -24,-57 -11,-49"/>
    <text class="burst-label" x="0" y="-4" font-size="17" text-anchor="middle">Reduced to</text>
    <text class="burst-price" x="0" y="33" font-size="38" text-anchor="middle">$10</text>
  </g>

  <g class="sale-headline">
    <text class="headline" x="495" y="316" font-size="116" textLength="598" lengthAdjust="spacingAndGlyphs">MASSIVE SALE</text>
    <text class="headline" x="493" y="366" font-size="44" textLength="602" lengthAdjust="spacingAndGlyphs">on this Easter Long Weekend</text>
  </g>

  <g class="service-hours">
    <text class="hours-label" x="238" y="437" font-size="15">Extended Customer Service hours:</text>
    <text class="hours-value" x="238" y="462" font-size="19">8am to 9pm Daily</text>
  </g>

  <g class="discount-offer">
    <text class="offer-small" x="557" y="446" font-size="24" textLength="70" lengthAdjust="spacingAndGlyphs">Up to</text>
    <text class="offer-big" x="632" y="463" font-size="58" textLength="140" lengthAdjust="spacingAndGlyphs">50%</text>
    <text class="offer-small" x="779" y="461" font-size="24" textLength="42" lengthAdjust="spacingAndGlyphs">Off</text>
  </g>

  <g class="view-products-button">
    <path fill="var(--button-red-dark)" d="M1122 396 L1140 398 L1136 418 Z"/>
    <path fill="var(--button-red-dark)" d="M926 488 L940 502 L952 494 Z"/>
    <rect x="910" y="393" width="226" height="104" rx="34" fill="url(#button-fill)"/>
    <text class="button-label" x="1021" y="434" font-size="24" text-anchor="middle">Click here to</text>
    <text class="button-label" x="1029" y="464" font-size="24" text-anchor="middle">view products</text>
  </g>
</svg>
</a>
</body>
</html>
```